Tobias Wrenfield - Cinematographer

NEED:
I'm looking for a sleek, professional, modern business card that will give give the recipient the impression that they can trust their production will go smoothly by hiring me. I will bring creativity and knowledge to their shoot, so that we can create powerful images.
I am looking for a card with a strong style and design ethos that could be expanded to a website and a full visual/graphic/design entity for me.
ABOUT ME:
I am a mid-twenties cinematographer, I work on music video, narrative short, commercial, and corporate projects. I blend the science and artistry of cameras and filmmaking to tell a story. I'm an artist, a technician, and a manager.
DESIGN:
I like sleek, simple design. Black, dark grays, white, dark navy, steel blues, I love cyan, but also cyan and red. I am not a fan of earthy tones. I generally prefer modern, san-serif fonts over serifs. My old logo was based on an aperture, a multi-blade device at the back of a lens that controls how much light passes through, but I made it with so many colors, that it doesn't necessarily lend itself to a specific color-scheme or design ethos. I liked that the aperture design provided a sense of the technical requirements of my job. I'm a fan of matte business cards, but am open to plenty of specialty print processes to make an outstanding card.
ATTACHED FILES:
My Old Rainbox Aperture Logo, plus a few designs I've tried playing around with, but am not tied to. I AM OPEN TO NEW DESIGNS, DO NOT FEEL TIED TO THIS.
**I've pulled my old logo down from the attached files, and instead attached other business cards I like, so as not to mislead you where I would like to go.
INFO:
Name: Tobias Wrenfield
Job: Cinematographer
Email: tkwrenfield@quillbox.example
Phone: 503.618.2907
Website: tobiaswrenfield.example
Updates
I'm adding some images of other cards that I like, and removing my old logo, since I'm looking for something new, and don't want that old logo to push anyone a certain direction.

```html
<!DOCTYPE html>
<html lang="en">
<head>
<meta charset="utf-8">
<title>Tobias Wrenfield – Cinematographer Business Card</title>
<link rel="stylesheet" href="https://fonts.googleapis.com/css2?family=Poiret+One&display=swap">
<style>
  :root {
    --backdrop: #e4e4e4;
    --card-white: #ffffff;
    --ink: #1c1c1c;
    --icon-fill: #333333;
    --dark-card-top: #3a3c3e;
    --dark-card-mid: #232425;
    --dark-card-edge: #121213;
    --silver: #d6d8da;
    --silver-shade: #8d9194;
  }
  * { margin: 0; padding: 0; box-sizing: border-box; }
  html, body {
    width: 1157px;
    height: 1200px;
    overflow: hidden;
    background: var(--backdrop);
  }
  .sheet {
    width: 1157px;
    height: 1200px;
    display: flex;
    flex-direction: column;
    align-items: center;
    justify-content: center;
    gap: 40px;
  }
  .card {
    position: relative;
    width: 860px;
    height: 540px;
    overflow: hidden;
    font-family: "Poiret One", sans-serif;
  }
  /* Front: contact side */
  .card--front {
    background: var(--card-white);
    color: var(--ink);
  }
  .card--front .identity {
    position: absolute;
    left: 90px;
    top: 44px;
  }
  .identity__name {
    font-size: 76px;
    line-height: 1;
    font-weight: 400;
    letter-spacing: 0.01em;
    white-space: nowrap;
  }
  .identity__role {
    font-size: 34px;
    line-height: 1;
    letter-spacing: 0.6em;
    margin-top: 10px;
    white-space: nowrap;
  }
  .contacts {
    position: absolute;
    left: 173px;
    top: 226px;
    list-style: none;
    display: flex;
    flex-direction: column;
    gap: 38px;
  }
  .contact {
    display: flex;
    align-items: center;
    gap: 30px;
    font-size: 38px;
    line-height: 1;
    white-space: nowrap;
  }
  .contact__icon {
    width: 68px;
    height: 68px;
    flex: none;
  }
  /* Back: name side */
  .card--back {
    background:
      radial-gradient(ellipse 70% 80% at 40% 25%, var(--dark-card-top) 0%, var(--dark-card-mid) 55%, var(--dark-card-edge) 100%);
    display: flex;
    align-items: center;
    justify-content: center;
  }
  .card--back .identity {
    text-align: left;
    color: var(--silver);
    text-shadow: 0 2px 2px rgba(0,0,0,0.7), 0 -1px 0 var(--silver-shade);
    margin-top: 60px;
  }
  .card--back .identity__role {
    margin-top: 14px;
  }
</style>
</head>
<body>
<main class="sheet">
  <section class="card card--front" aria-label="Business card front">
    <header class="identity">
      <h1 class="identity__name">Tobias Wrenfield</h1>
      <p class="identity__role">CINEMATOGRAPHER</p>
    </header>
    <ul class="contacts">
      <li class="contact contact--email">
        <svg class="contact__icon" viewBox="0 0 68 68" aria-hidden="true">
          <circle cx="34" cy="34" r="34" fill="var(--icon-fill)"/>
          <rect x="17" y="22" width="34" height="24" rx="1.5" fill="#fff"/>
          <path d="M17 23 L34 37 L51 23" fill="none" stroke="var(--icon-fill)" stroke-width="2.5"/>
          <path d="M17 45 L29 33 M51 45 L39 33" fill="none" stroke="var(--icon-fill)" stroke-width="2"/>
        </svg>
        <span>tkwrenfield@quillbox.example</span>
      </li>
      <li class="contact contact--phone">
        <svg class="contact__icon" viewBox="0 0 68 68" aria-hidden="true">
          <circle cx="34" cy="34" r="34" fill="var(--icon-fill)"/>
          <path d="M16 30 C16 20 52 20 52 30 L52 35 C52 37 50 38 48 37 L42 34 C40 33 40 31 40 29 C36 27 32 27 28 29 C28 31 28 33 26 34 L20 37 C18 38 16 37 16 35 Z" fill="#fff" transform="rotate(180 34 34) translate(0 -2)"/>
        </svg>
        <span>503.618.2907</span>
      </li>
      <li class="contact contact--web">
        <svg class="contact__icon" viewBox="0 0 68 68" aria-hidden="true">
          <circle cx="34" cy="34" r="34" fill="var(--icon-fill)"/>
          <g fill="none" stroke="#fff" stroke-width="2.5">
            <circle cx="34" cy="34" r="18"/>
            <ellipse cx="34" cy="34" rx="8" ry="18"/>
            <line x1="34" y1="16" x2="34" y2="52"/>
            <line x1="16" y1="34" x2="52" y2="34"/>
            <path d="M19 25 H49 M19 43 H49"/>
          </g>
        </svg>
        <span>tobiaswrenfield.example</span>
      </li>
    </ul>
  </section>

  <section class="card card--back" aria-label="Business card back">
    <div class="identity">
      <p class="identity__name">Tobias Wrenfield</p>
      <p class="identity__role">CINEMATOGRAPHER</p>
    </div>
  </section>
</main>
</body>
</html>
```